Full Service Outdoor Property Management Company

We are looking for a new and fresh business card design. My company has been in business for 26 years. Winter: We are a large snow and ice management company that does work for commercial, industrial and municipal clients. We have been named "Top 100 Snow Companies in the U.S." for numerous years. Summer: We provide complete landscape maintenance and landscape design and construction for both residential and commercial clients. We must incorporate our logo into card design as well as (in no particular order):
Employees name
Office: (417) 803-2765
Cell: (xxx) xxx-xxxx
brightfold.com
1879 Marigold, Dunmore OH 43052
(Something about 26 + years in business as well as "Top 100 snow contractors as stated above)
Target Market(s)
Winter: Commercial, Industrial, Municipal
Summer: Residential and Commercial
Industry/Entity Type
Construction
Contact Information for Business Card
This is a little challenging as we are using one card for essentially two companies that target different customers from summer to winter. Perhaps the back side could be split in two or something to highlight the different services?? I'm open to any ideas!! Looking forward to seeing what you come up with!
Requirements
Must have
- Logo
- (in no particular order)
- Employees name
- Office: (417) 803-2765
- Cell: (xxx) xxx-xxxx
- brightfold.com
- 1879 Marigold, Dunmore OH 43052
Nice to have
- Something about 26 + years in business
- "Top 100 Snow Contractors in the U.S."
Should not have
- Cheesy pictures of lawn mowers and snow plows

```html
<!DOCTYPE html>
<html lang="en">
<head>
<meta charset="utf-8">
<title>Brightfold Business Card</title>
<link rel="stylesheet" href="https://fonts.googleapis.com/css2?family=Open+Sans:wght@400;600;700&display=swap">
<style>
  :root {
    --page: #e9e7e3;
    --card-white: #ffffff;
    --card-blue: #3d8fd8;
    --green: #1f8a4c;
    --blue-text: #2f7fc7;
    --ink: #3b3b3b;
    --white: #ffffff;
  }
  * { box-sizing: border-box; margin: 0; padding: 0; }
  html, body { width: 1200px; height: 900px; overflow: hidden; }
  body {
    background: var(--page);
    font-family: "Open Sans", Arial, sans-serif;
    display: flex;
    align-items: center;
    justify-content: center;
    gap: 60px;
  }
  .card {
    position: relative;
    width: 525px;
    height: 300px;
    box-shadow: 0 6px 18px rgba(0,0,0,0.18);
  }

  /* Front */
  .card--front { background: var(--card-white); color: var(--ink); }
  .brand {
    position: absolute; left: 34px; top: 40px;
    display: flex; align-items: center; gap: 10px;
  }
  .brand__dot { width: 16px; height: 16px; border-radius: 50%; background: var(--green); }
  .brand__name { font-size: 36px; font-weight: 700; color: var(--green); letter-spacing: 0.5px; }
  .divider {
    position: absolute; left: 315px; top: 120px; width: 2px; height: 140px; background: var(--green);
  }
  .contact { position: absolute; left: 330px; top: 122px; list-style: none; font-size: 13px; }
  .contact li { display: flex; align-items: center; gap: 8px; height: 22px; }
  .contact svg { width: 13px; height: 13px; flex: none; }
  .address {
    position: absolute; left: 330px; top: 236px; width: 182px;
    font-size: 11.5px; white-space: nowrap;
    padding-bottom: 6px; border-bottom: 2px solid var(--green);
  }
  .person { position: absolute; left: 34px; top: 165px; }
  .person__name { font-size: 19px; font-weight: 700; color: var(--green); }
  .person__title { font-size: 13px; font-weight: 600; color: var(--blue-text); }
  .front-web {
    position: absolute; left: 34px; top: 240px; width: 260px;
    font-size: 14px; padding-top: 8px; border-top: 2px solid var(--green);
  }

  /* Back */
  .card--back { background: var(--card-blue); color: var(--white); text-align: center; }
  .back-brand {
    position: absolute; left: 0; right: 0; top: 30px;
    display: flex; justify-content: center; align-items: center; gap: 10px;
  }
  .back-brand .brand__dot { background: var(--white); }
  .back-brand .brand__name { color: var(--white); font-size: 34px; }
  .claims { position: absolute; left: 0; right: 0; top: 98px; font-size: 14px; line-height: 1.45; }
  .services {
    position: absolute; left: 50px; right: 50px; top: 160px;
    display: flex; justify-content: space-between; text-align: left;
  }
  .services h3 { font-size: 14px; font-weight: 700; margin-bottom: 4px; }
  .services ul { list-style: none; font-size: 12.5px; line-height: 1.5; }
  .services li::before { content: "• "; }
  .services .extra { padding-top: 22px; }
</style>
</head>
<body>
  <section class="card card--back" aria-label="Card back">
    <div class="back-brand">
      <span class="brand__dot"></span>
      <span class="brand__name">Brightfold</span>
    </div>
    <p class="claims">Service Provider For Over 26 Years<br>Top 100 Snow Companies in the U.S.</p>
    <div class="services">
      <div>
        <h3>Winter Services</h3>
        <ul><li>Snow Plowing</li><li>Salting</li><li>Ice Control</li></ul>
      </div>
      <div>
        <h3>Summer Services</h3>
        <ul><li>Mowing</li><li>Landscaping</li></ul>
      </div>
      <div class="extra">
        <ul><li>Shrub Trimming</li><li>Clean-ups</li></ul>
      </div>
    </div>
  </section>

  <section class="card card--front" aria-label="Card front">
    <div class="brand">
      <span class="brand__dot"></span>
      <span class="brand__name">Brightfold</span>
    </div>
    <div class="divider"></div>
    <ul class="contact">
      <li>
        <svg viewBox="0 0 14 14"><circle cx="7" cy="7" r="6.5" fill="none" stroke="#1f8a4c"/><path d="M4.5 3.8l1.4-.3.8 1.8-.9.7a5 5 0 0 0 2.2 2.2l.7-.9 1.8.8-.3 1.4c-3.3.2-6-2.5-5.7-5.7z" fill="#1f8a4c"/></svg>
        (417) 803-2765
      </li>
      <li>
        <svg viewBox="0 0 14 14"><rect x="4" y="1" width="6" height="12" rx="1.2" fill="#1f8a4c"/><rect x="5" y="2.5" width="4" height="7" fill="#fff"/></svg>
        (417) 803-5190
      </li>
      <li>
        <svg viewBox="0 0 14 14"><circle cx="7" cy="7" r="6" fill="#1f8a4c"/><path d="M1 7h12M7 1c-2.5 3-2.5 9 0 12M7 1c2.5 3 2.5 9 0 12" stroke="#fff" fill="none" stroke-width="0.9"/></svg>
        www.brightfold.com
      </li>
    </ul>
    <p class="address">1879 Marigold, Dunmore OH 43052</p>
    <div class="person">
      <p class="person__name">Your Name</p>
      <p class="person__title">Title</p>
    </div>
    <p class="front-web">www.brightfold.com</p>
  </section>
</body>
</html>
```